Beneath the Quiet Lanterns Book Cover Image Design

I need a design (image only) for my book that captures the essence of the title, Beneath The Quiet Lanterns; is captivating, enticing, eye catching, heart warming and inspiring. The essence of the book is about raw, authentic heartfelt sharing about both the blessings and challenges of life. I cover issues from mid-life spiritual crisis, suicidal depression, heart break, loss of purpose to fulfilling life dreams, experiencing the magic of life, spiritual awakening, receiving the support of loving family & friends, transformational moments and breakthroughs and ultimately self love and compassion.
These are some of things I envision:
bright
bold
raw
compelling
inticing
intimate
colourful: pink, red, purple, green???
simple
light
depth
radiance
evoking a feeling of hope, inspiration, warmth, intrigue, mystery,

Target Market(s)

I see my book appealing to many walks of life who are looking for hope and inspiration, people dealing with mid-life spiritual crisis, depression, etc. but especially speaking to middle aged professional women (30-50 years old), spiritual seekers, looking for inspiration and hope.

Industry/Entity Type

It Support

Requirements
Must have
• 1 heart radiating out or 2 hearts reflected or connected,
Nice to have
• wings on the hearts??, butterflies flying out of the hearts?? rays of light coming out of the hearts or from the connection, infinity symbol connected and/or woven into the heart(s)

```html
<!DOCTYPE html>
<html lang="en">
<head>
<meta charset="utf-8">
<title>Beneath the Quiet Lanterns – Cover</title>
<link rel="stylesheet" href="https://fonts.googleapis.com/css2?family=Cinzel:wght@500;600&display=swap">
<style>
  :root {
    --glow-yellow: #fbe27a;
    --glow-amber: #f6b84a;
    --glow-orange: #ee8a3a;
    --glow-red: #d9442b;
    --title-red: #d8231f;
    --title-white: #fffaf0;
    --heart-red: #e0201c;
    --butterfly-white: #ffffff;
  }
  html, body {
    margin: 0;
    padding: 0;
    width: 855px;
    height: 1200px;
    overflow: hidden;
    background: #ffffff;
  }
  .cover {
    position: relative;
    width: 855px;
    height: 1200px;
    overflow: hidden;
    background:
      radial-gradient(circle at 12% 92%, rgba(255,240,200,0.55) 0 60px, transparent 110px),
      radial-gradient(circle at 30% 82%, rgba(255,235,190,0.45) 0 50px, transparent 95px),
      radial-gradient(circle at 88% 74%, rgba(255,230,200,0.4) 0 55px, transparent 100px),
      radial-gradient(circle at 82% 12%, rgba(255,250,220,0.5) 0 45px, transparent 90px),
      radial-gradient(circle at 18% 8%, rgba(255,250,225,0.5) 0 55px, transparent 110px),
      radial-gradient(ellipse at 95% 95%, var(--glow-red) 0%, transparent 45%),
      radial-gradient(ellipse at 40% 35%, var(--glow-yellow) 0%, var(--glow-amber) 45%, var(--glow-orange) 80%, var(--glow-red) 110%);
  }
  .title {
    position: absolute;
    inset: 0;
    margin: 0;
    font-family: "Cinzel", "Times New Roman", serif;
    font-weight: 600;
    letter-spacing: 1px;
  }
  .title-line {
    position: absolute;
    display: block;
    white-space: nowrap;
    line-height: 1;
    text-shadow: 0 2px 6px rgba(150, 60, 0, 0.25);
  }
  .title-line--first {
    top: 82px;
    left: 385px;
    transform: translateX(-50%);
    font-size: 74px;
    color: var(--title-red);
  }
  .title-line--second {
    top: 165px;
    left: 385px;
    transform: translateX(-50%);
    font-size: 74px;
    color: var(--title-red);
  }
  .title-line--third {
    top: 252px;
    left: 440px;
    font-size: 62px;
    font-weight: 500;
    color: var(--title-white);
  }
  .heart-art {
    position: absolute;
    left: 0;
    top: 0;
    width: 855px;
    height: 1200px;
  }
</style>
</head>
<body>
  <main class="cover">
    <h1 class="title">
      <span class="title-line title-line--first">BENEATH</span>
      <span class="title-line title-line--second">THE QUIET</span>
      <span class="title-line title-line--third">LANTERNS</span>
    </h1>

    <svg class="heart-art" viewBox="0 0 855 1200" xmlns="http://www.w3.org/2000/svg">
      <defs>
        <radialGradient id="butterflyGlow" cx="50%" cy="50%" r="60%">
          <stop offset="0%" stop-color="var(--butterfly-white)" stop-opacity="0.85"/>
          <stop offset="100%" stop-color="var(--butterfly-white)" stop-opacity="0.55"/>
        </radialGradient>
      </defs>
      <path class="butterfly-heart" role="img"
            aria-label="Heart shape formed by a cluster of white butterflies"
            fill="url(#butterflyGlow)"
            d="M421 470 C380 360 230 330 140 380 C40 440 40 600 140 720 C230 830 350 920 421 1026 C500 920 620 830 710 720 C810 600 810 440 710 380 C610 330 460 360 421 470 Z"/>
      <path class="red-heart"
            fill="var(--heart-red)"
            d="M205 482 C185 438 118 424 98 470 C82 512 110 562 205 652 C300 562 328 512 312 470 C292 424 225 438 205 482 Z"/>
    </svg>
  </main>
</body>
</html>
```